Modern Innovative Business Card Design

We require a nice, modern, clean business card design, ready for upload to Cardomora. Our company develops online banking software solutions for small financial insitutions. The design should be clean, professional, but yet not "corporate boring". See www.fyrolt.com for an idea of business image and profile. The design should communicate innovation, be modern and fresh, yet look professional and established.

Target Market(s)

Finance industry, bankers, entrepreneurs

Industry/Entity Type

Financial

Contact Information for Business Card

Tobias Wendlerup
CEO

FYROLT BV
Lindenwerf 38
1027 HX Amsterdam
The Netherlands

Phone: +31 20 517 8036
Direct: +31 20 604 1758
Skype: tobias.fyrolt
ceo@fyrolt.com
www.fyrolt.com

Font styles to use
Sans Serif

Requirements
Must have
• Should look clean, modern and professional. File should be ready for upload to cardomora.
Should not have
• Boring standard corporate layout

```html
<!DOCTYPE html>
<html lang="en">
<head>
<meta charset="utf-8">
<title>FYROLT business card</title>
<link rel="stylesheet" href="https://fonts.googleapis.com/css2?family=Montserrat:wght@600&family=Open+Sans:wght@400&display=swap">
<style>
  :root {
    --backdrop: #6b7b7e;
    --frame: #252b2c;
    --card-light: #f4f5f5;
    --card-mid: #dfe2e2;
    --brand-slate: #485356;
    --panel-top: #3fdcb0;
    --panel-bottom: #35cfa3;
    --tab-white: #f7f7f7;
    --icon-dark: #2e3436;
    --text-white: #ffffff;
  }
  * { margin: 0; padding: 0; box-sizing: border-box; }
  html, body { width: 1200px; height: 720px; overflow: hidden; background: var(--backdrop); }
  .canvas { position: relative; width: 1200px; height: 720px; background: var(--backdrop); }
  .trim-frame {
    position: absolute; left: 40px; top: 40px; width: 1120px; height: 639px;
    background: var(--frame);
  }
  .card-face {
    position: absolute; left: 62px; top: 62px; width: 1076px; height: 596px;
    background: linear-gradient(135deg, var(--card-light) 0%, var(--card-mid) 45%, var(--card-light) 70%, var(--card-mid) 100%);
  }
  .wordmark {
    position: absolute; left: 0; top: 96px; width: 1200px; text-align: center;
    font-family: "Montserrat", sans-serif; font-weight: 600; font-size: 138px;
    letter-spacing: 6px; line-height: 1; color: var(--brand-slate);
  }
  .contact-panel {
    position: absolute; left: 299px; top: 259px; width: 602px; height: 420px;
    border-radius: 20px 20px 0 0;
    background: linear-gradient(160deg, var(--panel-top), var(--panel-bottom));
    box-shadow: 0 0 18px rgba(0,0,0,0.18);
  }
  .icon-tab {
    position: absolute; left: 290px; width: 103px; height: 80px;
    background: var(--tab-white); border-radius: 8px;
    box-shadow: 0 2px 6px rgba(0,0,0,0.15);
    display: flex; align-items: center; justify-content: center;
  }
  .icon-tab::before {
    content: ""; position: absolute; left: -4px; top: -10px; width: 40px; height: 12px;
    border-radius: 6px 6px 0 0; background: rgba(0,0,0,0.12); z-index: -1;
  }
  .tab-web { top: 307px; }
  .tab-phone { top: 432px; }
  .tab-place { top: 555px; }
  .contact-line {
    position: absolute; left: 299px; width: 676px; text-align: center;
    font-family: "Open Sans", sans-serif; font-weight: 400; color: var(--text-white);
    line-height: 1.25;
  }
  .contact-web { top: 305px; font-size: 31px; }
  .contact-phone { top: 449px; font-size: 38px; }
  .contact-address { top: 555px; font-size: 28px; }
</style>
</head>
<body>
<main class="canvas">
  <div class="trim-frame"></div>
  <section class="card-face" role="img" aria-label="Light grey low-poly triangle background pattern"></section>

  <h1 class="wordmark">FYROLT</h1>

  <div class="contact-panel" role="img" aria-label="Mint green panel with a faint hexagon pattern"></div>

  <div class="icon-tab tab-web">
    <svg width="46" height="36" viewBox="0 0 46 36" aria-hidden="true">
      <rect x="7" y="4" width="32" height="22" rx="2" fill="none" stroke="var(--icon-dark)" stroke-width="4"/>
      <rect x="1" y="28" width="44" height="5" rx="2" fill="var(--icon-dark)"/>
    </svg>
  </div>
  <div class="icon-tab tab-phone">
    <svg width="40" height="54" viewBox="0 0 40 54" aria-hidden="true">
      <path d="M8 3 L16 3 L18 16 L12 19 C13 28 17 36 22 41 L27 37 L37 45 L32 52 C18 50 4 30 2 12 Z" fill="var(--icon-dark)"/>
    </svg>
  </div>
  <div class="icon-tab tab-place">
    <svg width="40" height="56" viewBox="0 0 40 56" aria-hidden="true">
      <path d="M20 2 C9 2 2 10 2 20 C2 33 20 54 20 54 C20 54 38 33 38 20 C38 10 31 2 20 2 Z M20 13 A7 7 0 1 1 19.99 13 Z" fill="var(--icon-dark)" fill-rule="evenodd"/>
    </svg>
  </div>

  <p class="contact-line contact-web">sales@fyrolt.com<br>www.fyrolt.com</p>
  <p class="contact-line contact-phone">+31205178036</p>
  <p class="contact-line contact-address">Lindenwerf 38,1027 HX<br>Amsterdam,The Netherlands</p>
</main>
</body>
</html>
```